もっともイメージにあった作品でした。
たくさんのご応募ありがとうございました。
【海外取り寄せ商品の取引の流れ】を案内するバナーの作成をお願いいたします。 バナー作成の仕事の依頼
希望する色 特になし・その他
バナーサイズ
• 横700 縦は自由に作って下さい。
目的・概要
海外商品お取り寄せの案内用バナーを作成していただける方を募集します。
▽ターゲット
海外取り寄せ商品の流れがお客様に分かるように案内用のバナーを作成して頂きます。
お客様に分かりやすいように、レイアウトをお願い致します。
記載していただく内容は以下の通りです。
記載内容
【タイトル】
・海外取り寄せご購入の流れ
【内容】
・1.お客様からのご注文
お取り寄せ希望の商品をカートにお入れ下さい。
ご注意
※お客様都合によるキャンセル・返品は承り兼ねます。
※配送日時の指定は商品が弊社に到着してから承れます。到着したメールが届きましたらご連絡ください。
※商品仕様が変更される場合があります。
・2.現地への在庫確認・発注
お客様からご注文いただいた商品を現地メーカー、または海外正規代理店にオーダーいたします。
※海外との取引の為、時間差で完売となる場合がございます。予めご了承ください。
※決算方法が銀行振り込みの場合は、入金確認後に在庫確認・発注となります。
・3.現地より弊社へ出荷
現地より弊店宛に発送されましたら、メールにてご連絡いたします。
メーカーまたは海外正規代理店にオーダー後、入荷まで3週間~5週間ほど掛かります。
※商品や時期によって入荷までの期間が前後する場合がございます。
※空輸時のフライト状況、税関の混雑時などの理由により、遅れる場合もございます。
・4.入荷・検品・発送
メーカーより商品が弊店に入荷しましたら検品後、順次お客様へ発送いたします。
※2点以上のお買い上げの場合、準備ができた商品から順に発送いたします。
-上記内容をご理解の上、ご注文いただきますようお願いいたします-
※上記内容をお守り頂けませんと、商品の発送ができない場合がございます。
▽サイズ
横700 縦はお任せします。
▽参考デザイン
http://www.pallumora-shop.example/item/604927.html
http://item.vexadoru.example.jp/7q-garments/395061-214/
あくまで参考ですので、デザイン・配置などはお任せいたします。
【納品ファイル】
フォトショップ形式(.psd)でお願いします。
納品していただく際は、こちらでも編集できるようにお願いいたします。

```html
<!DOCTYPE html>
<html lang="ja">
<head>
<meta charset="utf-8">
<title>海外取り寄せご購入の流れ</title>
<link rel="stylesheet" href="https://fonts.googleapis.com/css2?family=Noto+Sans+JP:wght@400;700;900&display=swap">
<style>
  :root {
    --orange: #f39800;
    --orange-light: #f8b94a;
    --orange-pale: #fde3b4;
    --ink: #222;
    --alert: #d9000d;
    --paper: #fff;
  }
  * { box-sizing: border-box; margin: 0; padding: 0; }
  html, body { width: 1200px; height: 1200px; overflow: hidden; background: var(--paper); }
  body {
    font-family: "Noto Sans JP", sans-serif;
    color: var(--ink);
    display: grid;
    grid-template-columns: 1fr 1fr;
    grid-template-rows: 530px 170px 1fr;
    gap: 10px;
    padding: 0;
  }
  .step {
    border: 6px solid var(--orange);
    display: flex;
    flex-direction: column;
    background: var(--paper);
  }
  .step-title {
    background: var(--orange);
    color: #fff;
    font-weight: 900;
    font-size: 46px;
    line-height: 1;
    text-align: center;
    padding: 14px 0 18px;
    letter-spacing: 1px;
  }
  .step-lead {
    font-size: 20px;
    font-weight: 700;
    line-height: 1.55;
    padding: 14px 18px 0;
  }
  .flow {
    flex: 1;
    display: flex;
    align-items: center;
    justify-content: space-around;
    padding: 10px 18px;
  }
  .art {
    background: linear-gradient(160deg, var(--orange-light), var(--orange));
    border-radius: 10px;
  }
  .arrow { width: 70px; height: 60px; flex: none; }
  .notes {
    font-size: 15px;
    line-height: 1.6;
    padding: 0 18px 14px;
  }
  .notes h3 { font-size: 16px; font-weight: 700; }
  .notes p { padding-left: 1em; text-indent: -1em; }
  .band {
    grid-column: 1 / span 2;
    background: var(--orange);
    text-align: center;
    padding-top: 22px;
  }
  .band h1 { font-size: 64px; font-weight: 900; line-height: 1.1; letter-spacing: 2px; }
  .band .request { font-size: 19px; font-weight: 700; margin-top: 10px; }
  .band .warning { font-size: 17px; font-weight: 700; color: var(--alert); }
</style>
</head>
<body>

<section class="step">
  <h2 class="step-title">1.お客様からのご注文</h2>
  <p class="step-lead">お取り寄せ希望の商品をカートにお入れ下さい。</p>
  <div class="flow">
    <div class="art" style="width:230px;height:170px" role="img" aria-label="Tシャツ・サングラス・スニーカーのイラスト"></div>
    <svg class="arrow" viewBox="0 0 70 60"><polygon points="0,18 40,18 40,2 70,30 40,58 40,42 0,42" fill="var(--orange)"/></svg>
    <div class="art" style="width:150px;height:150px" role="img" aria-label="ショッピングカートのイラスト"></div>
  </div>
  <div class="notes">
    <h3>ご注意</h3>
    <p>※お客様都合によるキャンセル・返品は承り兼ねます。</p>
    <p>※配送日時の指定は商品が弊社に到着してから承れます。到着したメールが届きましたらご連絡ください。</p>
    <p>※商品仕様が変更される場合があります。</p>
  </div>
</section>

<section class="step">
  <h2 class="step-title">2.現地への在庫確認・発注</h2>
  <p class="step-lead">お客様からご注文いただいた商品を現地メーカー、または海外正規代理店にオーダーいたします。</p>
  <div class="flow">
    <div class="art" style="width:170px;height:150px" role="img" aria-label="パソコンのイラスト"></div>
    <svg class="arrow" viewBox="0 0 70 60"><polygon points="0,18 40,18 40,2 70,30 40,58 40,42 0,42" fill="var(--orange)"/></svg>
    <div class="art" style="width:140px;height:170px" role="img" aria-label="ビルのイラスト"></div>
  </div>
  <div class="notes">
    <h3>ご注意</h3>
    <p>※海外との取引の為、時間差で完売となる場合がございます。予めご了承ください。</p>
    <p>※決算方法が銀行振り込みの場合は、入金確認後に在庫確認・発注となります。</p>
  </div>
</section>

<div class="band">
  <h1>海外取り寄せご購入の流れ</h1>
  <p class="request">内容をご理解の上、ご注文いただきますようお願いいたします</p>
  <p class="warning">※内容をお守り頂けませんと、商品の発送ができない場合がございます。</p>
</div>

<section class="step">
  <h2 class="step-title">3.現地より弊社へ出荷</h2>
  <p class="step-lead" style="font-size:19px">現地より弊店宛に発送されましたら、メールにてご連絡いたします。<br>メーカーまたは海外正規代理店にオーダー後入荷まで3週間～5週間ほど掛かります。</p>
  <div class="flow">
    <div class="art" style="width:110px;height:120px" role="img" aria-label="ビルのイラスト"></div>
    <div class="art" style="width:130px;height:90px" role="img" aria-label="荷物を積んだトラックのイラスト"></div>
    <svg class="arrow" viewBox="0 0 70 60"><polygon points="0,18 40,18 40,2 70,30 40,58 40,42 0,42" fill="var(--orange)"/></svg>
    <svg width="120" height="86" viewBox="0 0 120 86" role="img" aria-label="メール">
      <rect x="4" y="4" width="112" height="78" fill="#fff" stroke="var(--orange)" stroke-width="6"/>
      <polyline points="4,4 60,48 116,4" fill="none" stroke="var(--orange)" stroke-width="6"/>
    </svg>
  </div>
  <div class="notes">
    <h3>ご注意</h3>
    <p>※商品や時期によって入荷までの期間が前後する場合がございます。</p>
    <p>※空輸時のフライト状況、税関の混雑時などの理由により、遅れる場合もございます。</p>
  </div>
</section>

<section class="step">
  <h2 class="step-title">4.入荷・検品・発送</h2>
  <p class="step-lead">メーカーより商品が弊店に入荷しましたら検品後、順次お客様へ発送いたします。</p>
  <div class="flow">
    <div class="art" style="width:90px;height:90px" role="img" aria-label="段ボール箱のイラスト"></div>
    <svg class="arrow" viewBox="0 0 70 60"><polygon points="0,18 40,18 40,2 70,30 40,58 40,42 0,42" fill="var(--orange)"/></svg>
    <div class="art" style="width:130px;height:100px" role="img" aria-label="配送トラックのイラスト"></div>
    <svg class="arrow" viewBox="0 0 70 60"><polygon points="0,18 40,18 40,2 70,30 40,58 40,42 0,42" fill="var(--orange)"/></svg>
    <div class="art" style="width:100px;height:100px" role="img" aria-label="家のイラスト"></div>
  </div>
  <div class="notes">
    <h3>ご注意</h3>
    <p>※2点以上のお買い上げの場合、準備ができた商品から順に発送いたします。</p>
  </div>
</section>

</body>
</html>
```